Engineering group involved with fire safety needs a business card

We need a business card design for a company based in Greece called "Varotis Group". We are engineers and specialized technicians, operating the following : a) Fire fighting equipment trade b) Installation , Inspection & Maintenance of fire extinguishers and fire protection systems c) Occupational Health & Safety (Risk assessment & management/ Staff training). We need a clear and simple card design. I uploaded a draft I made, in order to give you an idea of the company and how I currently imagine the design of the card. I also uploaded the logo in .png file format. We are always open to different, new suggestions and ideas you may want to submit.
Target Market(s)
industries, companies, managers, retail clients
Industry/Entity Type
Fire Safety
Contact Information for Business Card
Addresses & phone numbers (headquarters + branch), logo, name (you can find all the details on the uploaded files!)
Colors
Designer to choose colors to be used in the design.
Look and feel
Each slider illustrates characteristics of the customer's brand and the style your logo design should communicate.

```html
<!DOCTYPE html>
<html lang="el">
<head>
<meta charset="utf-8">
<title>Varotis Group – Business Card</title>
<link rel="stylesheet" href="https://fonts.googleapis.com/css2?family=Roboto:wght@400;500;700&display=swap">
<style>
  :root {
    --bg: #e9e6e1;
    --graphite: #4d4d4f;
    --signal-red: #e2292e;
    --white: #ffffff;
    --shadow: 0 1px 2px rgba(0,0,0,.45);
  }
  * { box-sizing: border-box; margin: 0; padding: 0; }
  html, body { width: 1200px; height: 790px; overflow: hidden; }
  body {
    background: var(--bg);
    font-family: "Roboto", Arial, sans-serif;
    color: var(--white);
    position: relative;
  }
  .card {
    position: absolute;
    top: 80px;
    width: 390px;
    height: 630px;
    background: var(--graphite);
    box-shadow: 0 3px 8px rgba(0,0,0,.25);
    overflow: hidden;
  }
  .card--front { left: 170px; }
  .card--back { left: 640px; }
  .card__panel { position: absolute; inset: 0; width: 100%; height: 100%; }
  .card__panel polygon { fill: var(--signal-red); }

  .brand { position: absolute; left: 0; right: 0; text-align: center; }
  .brand__mark {
    display: block; margin: 0 auto 14px;
    width: 26px; height: 26px; background: var(--signal-red);
  }
  .brand__name {
    color: var(--signal-red); font-weight: 700; line-height: 1;
    letter-spacing: 1px;
  }
  .brand__tagline { color: var(--white); font-weight: 400; margin-top: 10px; }

  .card--front .brand { top: 80px; }
  .card--front .brand__name { font-size: 44px; }
  .card--front .brand__tagline { font-size: 13px; }

  .card--back .brand { top: 70px; }
  .card--back .brand__mark { width: 22px; height: 22px; margin-bottom: 12px; }
  .card--back .brand__name { font-size: 36px; }
  .card--back .brand__tagline { font-size: 11px; margin-top: 8px; }

  .services {
    position: absolute; left: 40px; right: 0; top: 340px;
    list-style: none; text-align: center;
  }
  .services li {
    font-size: 16px; font-weight: 700; letter-spacing: .2px;
    height: 48px; text-shadow: var(--shadow);
  }
  .front-contact {
    position: absolute; left: 40px; right: 0; top: 550px;
    text-align: center; font-size: 16px; font-weight: 500; line-height: 28px;
    text-shadow: var(--shadow);
  }

  .person { position: absolute; left: 0; right: 0; top: 258px; text-align: center; text-shadow: var(--shadow); }
  .person__name { font-size: 26px; font-weight: 700; letter-spacing: .3px; }
  .person__role { font-size: 15px; margin-top: 10px; }
  .person__subrole { font-size: 10.5px; margin-top: 10px; }

  .contact { position: absolute; left: 0; right: 0; }
  .contact__icon {
    position: absolute; left: 21px; width: 26px; height: 26px;
  }
  .contact__lines {
    position: absolute; left: 58px; font-size: 14px; line-height: 27.5px;
    white-space: nowrap; text-shadow: var(--shadow);
  }
  .contact--phone { top: 376px; }
  .contact--phone .contact__icon { top: 12px; }
  .contact--mail { top: 468px; }
  .contact--mail .contact__icon { top: 1px; }
  .contact--address { top: 506px; }
  .contact--address .contact__icon { top: 10px; }
  .contact--address .contact__lines { font-size: 13px; line-height: 21px; }
  .back-web {
    position: absolute; left: 53px; right: 0; top: 577px; text-align: center;
    font-size: 16px; font-weight: 500; text-shadow: var(--shadow);
  }
</style>
</head>
<body>

<section class="card card--front" aria-label="Card front">
  <svg class="card__panel" viewBox="0 0 390 630" preserveAspectRatio="none" aria-hidden="true">
    <polygon points="53,340 390,143 390,630 53,630"/>
  </svg>
  <div class="brand">
    <span class="brand__mark"></span>
    <div class="brand__name">VAROTIS GROUP</div>
    <div class="brand__tagline">installation - inspection - maintenance</div>
  </div>
  <ul class="services">
    <li>ΕΞΟΠΛΙΣΜΟΣ ΠΥΡΑΣΦΑΛΕΙΑΣ</li>
    <li>ΑΔΕΙΟΔΟΤΗΣΗ ΕΠΙΧΕΙΡΗΣΕΩΝ</li>
    <li>ΕΠΑΓΓΕΛΜΑΤΙΚΗ ΑΣΦΑΛΕΙΑ</li>
    <li>ΕΚΠΑΙΔΕΥΣΗ ΠΡΟΣΩΠΙΚΟΥ</li>
  </ul>
  <div class="front-contact">
    <div>www.varotisgroup.gr</div>
    <div>info@varotisgroup.gr</div>
  </div>
</section>

<section class="card card--back" aria-label="Card back">
  <svg class="card__panel" viewBox="0 0 390 630" preserveAspectRatio="none" aria-hidden="true">
    <polygon points="53,345 390,140 390,630 53,630"/>
  </svg>
  <div class="brand">
    <span class="brand__mark"></span>
    <div class="brand__name">VAROTIS GROUP</div>
    <div class="brand__tagline">installation - inspection - maintenance</div>
  </div>
  <div class="person">
    <div class="person__name">ΝΙΚΟΛΑΟΣ ΒΑΡΩΤΗΣ</div>
    <div class="person__role">Μηχανολόγος Μηχανικός</div>
    <div class="person__subrole">Σύμβουλος Επαγγελματικής Υγείας &amp; Ασφάλειας</div>
  </div>

  <div class="contact contact--phone">
    <svg class="contact__icon" viewBox="0 0 26 26" aria-hidden="true">
      <circle cx="13" cy="13" r="13" fill="var(--signal-red)"/>
      <path d="M9 7.5c.6-.4 1.3-.3 1.6.3l1.2 2.2c.3.5.1 1.1-.3 1.4l-.8.6c.6 1.5 1.7 2.7 3.2 3.4l.6-.8c.4-.4 1-.6 1.4-.3l2.2 1.2c.6.3.7 1 .3 1.6l-.9 1.1c-.6.7-1.6.9-2.5.5-3.2-1.4-5.6-3.9-6.9-7-.4-.9-.2-1.9.5-2.5z" fill="var(--white)"/>
    </svg>
    <div class="contact__lines">
      <div>(Κεντρ.)&nbsp; 22910 48302</div>
      <div>(Υποκ.)&nbsp; 210 7429158</div>
      <div>Κιν.&nbsp; 694 215 30 48</div>
    </div>
  </div>

  <div class="contact contact--mail">
    <svg class="contact__icon" viewBox="0 0 26 26" aria-hidden="true">
      <circle cx="13" cy="13" r="13" fill="var(--signal-red)"/>
      <rect x="7" y="9" width="12" height="8.5" rx="1" fill="var(--white)"/>
      <path d="M7.5 9.5 13 14l5.5-4.5" fill="none" stroke="var(--signal-red)" stroke-width="1.2"/>
    </svg>
    <div class="contact__lines">nikolaos.varotis@varotisgroup.gr</div>
  </div>

  <div class="contact contact--address">
    <svg class="contact__icon" viewBox="0 0 26 26" aria-hidden="true">
      <circle cx="13" cy="13" r="13" fill="var(--signal-red)"/>
      <path d="M13 6.5a4.5 4.5 0 0 0-4.5 4.5c0 3.4 4.5 8.5 4.5 8.5s4.5-5.1 4.5-8.5A4.5 4.5 0 0 0 13 6.5z" fill="var(--white)"/>
      <circle cx="13" cy="11" r="1.7" fill="var(--signal-red)"/>
    </svg>
    <div class="contact__lines">
      <div>Κεντρικό: Ανδρέα Λεβίδη 12, Κερατέα, 19001</div>
      <div>Υποκατ/μα: Κηφισίας 84, Χαλάνδρι, 15233</div>
    </div>
  </div>

  <div class="back-web">www.varotisgroup.gr</div>
</section>

</body>
</html>
```